Tarnel-Holdings. Limestone; improving the world

New Limestone company and need logo design.
Limestone offsets carbon mitigation industries restore and replenish soil fertilities in the Prairies, the breadbasket of the world. At the same time, Limestone is proving a critical emergent component of carbon capture sequestration technology will therefore play a critical role in the development of the western Canadian energy industries
Our limestone resources are situated in the foothills of the Canadian Rockies well-positioned above the sprawling fields of the vast peace district.
Target Market(s)
Agriculture and oli sites
Logo Text
Tarnel Holdings
Number of Pages Required
3 page

```html
<!DOCTYPE html>
<html lang="en">
<head>
<meta charset="utf-8">
<title>Tarnel Holdings — Limestone</title>
<link href="https://fonts.googleapis.com/css2?family=Domine:wght@400;700&family=Roboto:wght@400;500&display=swap" rel="stylesheet">
<style>
:root{
  --teal:#3a9ac4;
  --slate:#4e7189;
  --forest:#2f6e5b;
  --dark:#1f3b3a;
  --card:#f0f3f3;
  --band:#f7f7f7;
  --yellow:#e6d44c;
  --text:#555;
  --white:#fff;
}
*{margin:0;padding:0;box-sizing:border-box}
html,body{width:1200px;height:4366px;overflow:hidden}
body{position:relative;background:var(--white);font-family:'Roboto',sans-serif;color:var(--text)}
.abs{position:absolute}
.serif{font-family:'Domine',serif}

/* hero */
.hero{left:0;top:0;width:1200px;height:730px;background:linear-gradient(180deg,#6d8287 0%,#4f6a66 45%,#5d6c68 75%,#6f7471 100%)}
.brand{left:68px;top:22px;display:flex;align-items:center;gap:14px}
.brand-dot{width:58px;height:58px;border-radius:50%;background:var(--forest)}
.brand-name{font-family:'Domine',serif;font-weight:700;font-size:24px;line-height:26px;color:var(--white)}
.nav{top:34px;left:651px;display:flex;gap:0;font-size:16px;color:var(--white)}
.nav span{position:absolute;white-space:nowrap}
.contact-btn{left:992px;top:25px;width:140px;height:43px;border-radius:22px;background:var(--white);color:var(--slate);font-family:'Domine',serif;font-weight:700;font-size:12px;display:flex;align-items:center;justify-content:center;gap:6px}
.hero-title{left:68px;top:222px;font-family:'Domine',serif;font-weight:700;font-size:68px;line-height:72px;color:var(--white);letter-spacing:-2px}
.know-btn{left:68px;top:502px;width:161px;height:54px;border-radius:27px;background:var(--slate);border:2px solid #8fb0c2;color:var(--white);font-family:'Domine',serif;font-weight:700;font-size:15px;display:flex;align-items:center;justify-content:center}
.or{left:257px;top:518px;font-family:'Domine',serif;font-size:17px;color:#e6eaea}
.hero-phone{left:305px;top:516px;font-family:'Domine',serif;font-weight:700;font-size:19px;color:var(--white);display:flex;align-items:center;gap:8px}

/* solution */
.solution-img{left:0;top:730px;width:614px;height:575px;background:linear-gradient(135deg,#3b302a 0%,#6aa931 35%,#4b3d33 60%,#c89a7c 80%,#3f342e 100%)}
.play{border-radius:50%;display:flex;align-items:center;justify-content:center}
.solution-title{left:702px;top:858px;width:440px;font-family:'Domine',serif;font-weight:700;font-size:49px;line-height:66px;color:var(--teal);letter-spacing:-1px}
.solution-text{left:702px;top:1047px;width:390px;font-size:14px;line-height:29px;color:var(--text)}

/* cards */
.card{top:1403px;width:244px;height:267px;background:var(--card);text-align:center}
.card.active{height:326px;background:var(--slate)}
.card svg{margin-top:52px}
.card h3{font-family:'Domine',serif;font-weight:700;font-size:18px;color:#222;margin-top:22px}
.card p{font-size:14px;line-height:29px;color:#666}
.card .first{margin-top:10px}
.card.active h3{color:var(--white)}
.card.active p{color:#c9d6df}
.explore{font-family:'Domine',serif;font-weight:700;font-size:14px;color:var(--white);text-decoration:underline;margin-top:21px;display:inline-block}

/* liming */
.band{left:0;top:1793px;width:1200px;height:505px;background:var(--band)}
.liming-title{left:68px;top:1895px;font-family:'Domine',serif;font-weight:700;font-size:58px;line-height:84px;color:var(--teal)}
.learn-btn{left:970px;top:1946px;width:162px;height:57px;border:2px solid var(--forest);border-radius:29px;color:var(--forest);font-family:'Domine',serif;font-weight:700;font-size:15px;display:flex;align-items:center;justify-content:center}
.quarry-img{left:230px;top:2134px;width:543px;height:383px;background:linear-gradient(180deg,#6ab5e6 0%,#a9d3ef 45%,#8c8d8a 62%,#6f706b 100%)}
.quote{left:69px;top:2208px;width:323px;height:234px;background:var(--forest);padding:38px 40px 0;color:var(--white)}
.stars{color:#f3c316;font-size:17px;letter-spacing:4px}
.quote q{display:block;font-family:'Domine',serif;font-size:18px;line-height:27px;margin-top:14px}
.quote cite{display:block;font-style:normal;font-size:13px;margin-top:8px}

/* stats */
.apply-title{left:68px;top:2657px;width:450px;font-family:'Domine',serif;font-weight:700;font-size:30px;line-height:45px;color:var(--teal)}
.apply-text{left:68px;top:2813px;width:420px;font-size:14px;line-height:29px}
.stat{display:flex;gap:20px;align-items:flex-start}
.stat b{display:block;font-family:'Domine',serif;font-weight:700;font-size:22px;color:#222}
.stat small{display:block;font-size:14px;color:#666;margin-top:4px}

/* newsletter */
.news-bg{left:29px;top:3056px;width:1171px;height:805px;background:linear-gradient(180deg,#e2e4e3 0%,#d2d6d4 35%,#8c9c8e 60%,#4f6e48 85%,#3f5f3c 100%)}
.news-title{left:68px;top:3140px;font-family:'Domine',serif;font-weight:700;font-size:22px;color:var(--teal)}
.news-text{left:68px;top:3182px;width:430px;font-size:14px;line-height:29px}
.field{left:68px;width:349px;height:53px;background:var(--white);font-family:'Domine',serif;font-size:14px;color:#666;padding:17px 19px}
.call-btn{left:68px;top:3454px;width:251px;height:58px;border-radius:29px;background:var(--slate);color:var(--white);font-family:'Domine',serif;font-weight:700;font-size:16px;display:flex;align-items:center;justify-content:center}

/* footer */
.footer{left:0;top:3861px;width:1200px;height:505px;background:var(--slate)}
.left-strip{left:0;top:3760px;width:29px;height:101px;background:var(--slate)}
.foot-brand{left:68px;top:3922px;display:flex;align-items:center;gap:14px}
.foot-brand .brand-dot{width:74px;height:74px;background:#5a9a7f}
.foot-brand .brand-name{font-size:31px;line-height:34px}
.badge-a{left:181px;top:4000px;width:104px;height:82px;background:#c8333a;border-radius:6px}
.badge-b{left:345px;top:4012px;width:62px;height:62px;border-radius:50%;background:#b8342e}
.copy{left:68px;top:4153px;font-size:12px;color:var(--yellow)}
.foot-head{font-size:14px;color:var(--yellow)}
.feed{left:614px;top:3963px;width:327px;height:122px;background:linear-gradient(90deg,#3d4f63,#8a7d79 50%,#c9cbcf)}
.contact-title{left:614px;top:4102px;font-family:'Domine',serif;font-weight:700;font-size:34px;color:var(--yellow)}
.contact-line{left:614px;font-size:13px;color:var(--yellow)}
.links{left:978px;top:3966px;font-family:'Domine',serif;font-size:18px;line-height:43px;color:#dfe7ec}
</style>
</head>
<body>

<section class="abs hero" role="img" aria-label="Mountain valley with pine forest and rocky river gorge"></section>
<div class="abs brand"><span class="brand-dot"></span><span class="brand-name">Tarnel<br>Holdings</span></div>
<nav class="abs nav" style="left:0;width:1200px">
  <span style="left:651px">HOME</span><span style="left:737px">ABOUT</span><span style="left:829px">TEAM</span><span style="left:912px">FAQ´S</span>
</nav>
<div class="abs contact-btn">
  <svg width="13" height="10" viewBox="0 0 13 10"><rect x=".5" y=".5" width="12" height="9" fill="none" stroke="currentColor"/><path d="M.5 .5 6.5 5.5 12.5 .5" fill="none" stroke="currentColor"/></svg>CONTACT US
</div>
<h1 class="abs hero-title">Know the<br>results of<br>the Limestone.</h1>
<div class="abs know-btn">Know more</div>
<div class="abs or">or</div>
<div class="abs hero-phone">
  <svg width="18" height="18" viewBox="0 0 24 24"><path fill="#fff" d="M6.6 10.8a15.1 15.1 0 0 0 6.6 6.6l2.2-2.2c.3-.3.7-.4 1-.2 1.1.4 2.3.6 3.6.6.6 0 1 .4 1 1V20c0 .6-.4 1-1 1A17 17 0 0 1 3 4c0-.6.4-1 1-1h3.5c.6 0 1 .4 1 1 0 1.3.2 2.5.6 3.6.1.3 0 .7-.2 1z"/></svg>
  +1 403 555 0192
</div>

<section class="abs solution-img" role="img" aria-label="Heart shape of green sprouts on dark soil beside a cupped hand"></section>
<div class="abs play" style="left:120px;top:976px;width:70px;height:70px;background:rgba(255,255,255,.25)">
  <svg width="28" height="30" viewBox="0 0 28 30"><path d="M2 1 27 15 2 29z" fill="var(--teal)"/></svg>
</div>
<h2 class="abs solution-title">What solution are you looking for?</h2>
<p class="abs solution-text">I'm a testimonial. Click to edit me and add text that says something nice about you and your services. Let your customers review you and tell their friends.</p>

<div class="abs card" style="left:59px">
  <svg width="30" height="40" viewBox="0 0 30 40"><circle cx="15" cy="8" r="6" fill="var(--forest)"/><path d="M15 40V14M15 26C6 26 2 20 2 16c6 0 13 3 13 10zm0 0c9 0 13-6 13-10-6 0-13 3-13 10z" fill="var(--forest)" stroke="var(--forest)"/></svg>
  <h3>Friable Limestone</h3><p class="first">Know more</p><p>What you looking for.</p>
</div>
<div class="abs card active" style="left:332px">
  <svg width="30" height="40" viewBox="0 0 30 40"><circle cx="15" cy="8" r="6" fill="#fff"/><path d="M15 40V14M15 26C6 26 2 20 2 16c6 0 13 3 13 10zm0 0c9 0 13-6 13-10-6 0-13 3-13 10z" fill="#fff" stroke="#fff"/></svg>
  <h3>Dry Limestone</h3><p class="first">Know more</p><p>What you looking for.</p>
  <span class="explore">Explore Now</span> <svg width="10" height="10" viewBox="0 0 10 10"><path d="M3 1 7 5 3 9" stroke="#fff" stroke-width="2" fill="none"/></svg>
</div>
<svg class="abs" style="left:522px;top:1640px" width="42" height="76" viewBox="0 0 42 76"><path d="M2 2V62L15 50 25 74 33 70 23 47H40z" fill="#fff" stroke="#333" stroke-width="1.5"/></svg>
<div class="abs card" style="left:607px">
  <svg width="30" height="40" viewBox="0 0 30 40"><circle cx="15" cy="8" r="6" fill="var(--forest)"/><path d="M15 40V14M15 26C6 26 2 20 2 16c6 0 13 3 13 10zm0 0c9 0 13-6 13-10-6 0-13 3-13 10z" fill="var(--forest)" stroke="var(--forest)"/></svg>
  <h3>Pebble</h3><p class="first">Know more</p><p>What you looking for.</p>
</div>
<div class="abs card" style="left:880px">
  <svg width="30" height="40" viewBox="0 0 30 40"><circle cx="15" cy="8" r="6" fill="var(--forest)"/><path d="M15 40V14M15 26C6 26 2 20 2 16c6 0 13 3 13 10zm0 0c9 0 13-6 13-10-6 0-13 3-13 10z" fill="var(--forest)" stroke="var(--forest)"/></svg>
  <h3>Artificial Sand</h3><p class="first">Know more</p><p>What you looking for.</p>
</div>

<section class="abs band"></section>
<h2 class="abs liming-title">The importance of liming<br>for the soil.</h2>
<div class="abs learn-btn">Learn More</div>
<div class="abs quarry-img" role="img" aria-label="Conveyor belt piling crushed limestone into a large heap under blue sky"></div>
<div class="abs play" style="left:471px;top:2293px;width:68px;height:68px;background:rgba(255,255,255,.85)">
  <svg width="22" height="24" viewBox="0 0 22 24"><path d="M2 1 21 12 2 23z" fill="var(--teal)"/></svg>
</div>
<blockquote class="abs quote">
  <div class="stars">★★★★★</div>
  <q>Many of life’s failures are people who did not realize how to success.</q>
  <cite>- Dara Wollen , School Teacher</cite>
</blockquote>

<h2 class="abs apply-title">The application of limestone increases the results of agricultural production.</h2>
<p class="abs apply-text">Credibly benchmark worldwide applications before a plug play processes dramatically.</p>
<div class="abs stat" style="left:622px;top:2672px">
  <svg width="48" height="48" viewBox="0 0 48 48"><circle cx="24" cy="24" r="23" fill="#dfe8e4"/><path d="M24 8 28 20 40 24 28 28 24 40 20 28 8 24 20 20z" fill="var(--dark)"/></svg>
  <div><b>15+</b><small>Location Service</small></div>
</div>
<div class="abs stat" style="left:895px;top:2672px">
  <svg width="48" height="48" viewBox="0 0 48 48"><circle cx="24" cy="28" r="18" fill="#dfe8e4"/><path d="M6 18c10-8 26-8 36 0l-4 6-6-2v-4c-5-2-11-2-16 0v4l-6 2z" fill="var(--dark)"/><rect x="12" y="24" width="24" height="16" rx="4" fill="var(--dark)"/><circle cx="24" cy="32" r="4" fill="#dfe8e4"/></svg>
  <div><b>24/7</b><small>Customer care</small></div>
</div>
<div class="abs stat" style="left:622px;top:2803px">
  <svg width="48" height="48" viewBox="0 0 48 48"><path d="M2 44 24 14 46 44z" fill="#dfe8e4"/><path d="M10 44 24 24 38 44z" fill="var(--dark)"/><path d="M24 24V6l10 4-10 4" fill="var(--dark)" stroke="var(--dark)"/></svg>
  <div><b>08+</b><small>Years Experience</small></div>
</div>
<div class="abs stat" style="left:895px;top:2803px">
  <svg width="50" height="48" viewBox="0 0 50 48"><path d="M2 4h26v16c0 10-6 16-13 16S2 30 2 20z" fill="#dfe8e4"/><path d="M18 14h28v16c0 10-6 16-14 16s-14-6-14-16z" fill="var(--dark)"/><circle cx="26" cy="24" r="2.5" fill="#fff"/><circle cx="38" cy="24" r="2.5" fill="#fff"/><path d="M25 34q7 5 14 0" stroke="#fff" stroke-width="2" fill="none"/></svg>
  <div><b>1.8 M+</b><small>Happy Clients</small></div>
</div>

<div class="abs left-strip"></div>
<section class="abs news-bg" role="img" aria-label="Misty forested karst mountains"></section>
<h2 class="abs news-title">Newsletters</h2>
<p class="abs news-text">We continually invest in materials that generate information so your customers are always well informed.</p>
<div class="abs field" style="top:3270px">Name</div>
<div class="abs field" style="top:3351px">Phone Number</div>
<div class="abs call-btn">Request For Call</div>

<footer class="abs footer"></footer>
<div class="abs foot-brand"><span class="brand-dot"></span><span class="brand-name">Tarnel<br>Holdings</span></div>
<div class="abs badge-a"></div>
<div class="abs badge-b"></div>
<p class="abs copy">© 2021 Tarnel-Holdings.</p>
<h4 class="abs foot-head" style="left:614px;top:3910px;font-weight:400">Social Feed</h4>
<div class="abs feed" role="img" aria-label="Social page preview with photo thumbnails"></div>
<h3 class="abs contact-title">Contact Us</h3>
<p class="abs contact-line" style="top:4152px">Phone: 403-555-0148</p>
<p class="abs contact-line" style="top:4174px">Email: hello@tarnel-holdings.example</p>
<h4 class="abs foot-head" style="left:978px;top:3910px;font-weight:400">Quick Links</h4>
<nav class="abs links">Home<br>About<br>Team<br>FAQ´s</nav>

</body>
</html>
```